we can communicate on this, but i want to follow the approach we took on Pellow|Quint & Marsh but i feel the card front needs the black background and the platinum and gold logo. The back? I am open. we can use the same info from PQ&M. Velmora Point is an enhanced equity investment fund - basically a very exclusive boutique hedge fund that uses only stock options. very advanced things. hope you are interested

Contact Information for Business Card

Dr. Lewis T. Brennick, CFA
Scientifique de fusée financière
701.555.0143
LBdoc4490@mailvex.example

4817 Birch Hollow Way W.
West Fargo, ND 58099

No web site

Colors

Designer to choose colors to be used in the design.

Requirements
Nice to have
• I tend to prefer the most visible applications of the logo to include logo and name, the logo version with a black background and the gold and platinum components separated by the black. I see this working well for a single side (logo and name - this is card front to me).
• I am fairly open to other treatments on the reverse side with the data. To me, it makes sense to have a different color rendition of the logo on the reverse and it may be a muted black tone on tone or an oversized portion that would have spot UV. Or, the reverse may play with colors and layout
Should not have
• Other colors = no no
• Decorative font

```html
<!DOCTYPE html>
<html lang="en">
<head>
<meta charset="utf-8">
<title>Velmora Point – Business Card</title>
<link href="https://fonts.googleapis.com/css2?family=Open+Sans:wght@400;700&display=swap" rel="stylesheet">
<style>
  :root {
    --backdrop: #dcd9d4;
    --card: #1c1c1c;
    --gold: #d4a82c;
    --ink-light: #f2f2f2;
    --rule: #e6e6e6;
  }
  * { margin: 0; padding: 0; box-sizing: border-box; }
  html, body {
    width: 1200px; height: 1000px; overflow: hidden;
    background: var(--backdrop);
    font-family: "Open Sans", Arial, sans-serif;
  }
  .card {
    position: absolute;
    width: 666px; height: 397px;
    background: var(--card);
    box-shadow: 0 6px 18px rgba(0,0,0,.35);
    color: var(--ink-light);
  }
  .card--info { left: 262px; top: 74px; }
  .card--brand { left: 267px; top: 533px; }

  .brand-mark {
    position: absolute;
    border-radius: 50%;
    background: var(--gold);
  }
  .brand-name {
    position: absolute;
    text-align: center;
    font-weight: 700;
    color: var(--ink-light);
    line-height: 1;
  }
  .brand-name .line-sub { display: block; }

  .card--info .brand-mark { left: 456px; top: 36px; width: 104px; height: 104px; }
  .card--info .brand-name { left: 378px; top: 166px; width: 260px; font-size: 40px; }
  .card--info .brand-name .line-sub { font-size: 20px; letter-spacing: 4px; margin-top: 6px; }

  .holder-name {
    position: absolute; left: 46px; top: 236px;
    font-size: 18px; font-weight: 400; color: var(--gold);
    letter-spacing: .3px; white-space: nowrap;
  }
  .divider {
    position: absolute; left: 46px; top: 268px;
    width: 576px; height: 2px; background: var(--rule);
  }
  .contact {
    position: absolute; left: 46px; top: 280px;
    list-style: none; font-size: 16px; line-height: 24.5px;
    color: var(--ink-light); white-space: nowrap;
  }

  .card--brand .brand-mark { left: 258px; top: 20px; width: 150px; height: 150px; }
  .card--brand .brand-name { left: 133px; top: 243px; width: 400px; font-size: 54px; }
  .card--brand .brand-name .line-sub { font-size: 27px; letter-spacing: 5px; margin-top: 8px; }
</style>
</head>
<body>
  <section class="card card--info">
    <div class="brand-mark" aria-hidden="true"></div>
    <div class="brand-name">VELMORA<span class="line-sub">POINT</span></div>
    <p class="holder-name">DR. LEWIS T. BRENNICK, CFA</p>
    <div class="divider"></div>
    <ul class="contact">
      <li>Scientifique de fusée financière</li>
      <li>701.555.0143</li>
      <li>LBdoc4490@mailvex.example</li>
      <li>4817 Birch Hollow Way W., West Fargo, ND 58099</li>
    </ul>
  </section>

  <section class="card card--brand">
    <div class="brand-mark" aria-hidden="true"></div>
    <div class="brand-name">VELMORA<span class="line-sub">POINT</span></div>
  </section>
</body>
</html>
```